Concept design for a tea business Labels

Hello, we are looking for concepts for our label/packaging for a tea business that has been in business now for over a year. We are a beachy, organic, "It's your moment. Enjoy it." type tea business. We have an online website (www.corvalbrewhouse.com.au) and sell at local markets around the Tarrowby Cove area.
We are looking to upgrade our label to look more professional, in a fun/beachy/chilled out style. (unlike the traditional tea labels).
We do loose leaf tea and iced tea consentrated syrups. We have a few different packages (please see website under "sizes and packaging" bottom left). We would like to experiement with various different size and shape of labels for different products, so would like a concept design for a label using our logo (see website front page bottom). There are no colour constraints.
We use the Quillan brand labels of the following sizes:
1. Pure Glass Rectangular Product Labels, Q4825, 100/Pack, 96 x 50.8 mm
2. Pure Glass Round Multi-purpose Labels, Q3907D, 240/Pack, 40 mm diameter
3.Pure Glass Square Product Labels, Q4861, 350/Pack, 35 x 35 mm
4. For bottles we use Grained Ivory Curved Labels, Q4839, 90/Pack, 57.2 x 77 mm
If you have any more questions, please don't hesitate to contact me
Updates
Hi All,
I am considering using a box like below for packing and doing a bit of a white/beachy feel to the packaging. Either using the rectangle or round circle labels. (circle labels from quillan 60mm diameter).

Reason: Hi All - Thank you so much for all your designs. While I have seen some really beautiful designs I am excited about, it seems there was a rush at the end with a number of new designs just submitted. I still haven't seen just one design I love for the label, so I would like the opportunity to work with some of the new designers to see if we can modify to suit the concept.
Would anyone like to try a concept label with a silhouette of one of the following wave/beach/teacup? I'm just exploring a different approach as I know it is difficult tying in the beach with tea - please think - chilled out beach hut with tea/iced tea, sunrise over ocean. I like the soft colour palette - beachy feel to it - ie. Pastels - blues, greens, whites, sandy, pinks, purples, greys - sunrises over ocean, maybe a white rustic wood feel - or any other icon from Tarrowby Cove - like the Norfolk Pine's along the beach - maybe in Silhouette.
Just some more ideas.
Thank you again for all your contributions!
Petra

```html
<!DOCTYPE html>
<html lang="en">
<head>
<meta charset="utf-8">
<title>Tarrowby Tea Company – Label Concepts</title>
<link rel="stylesheet" href="https://fonts.googleapis.com/css2?family=Noto+Serif:wght@400;700&display=swap">
<style>
  :root {
    --page: #ffffff;
    --ink: #1a1a1a;
    --shadow: rgba(40, 40, 40, 0.55);
    --teal: #33b6af;
    --teal-soft: #80c6ac;
    --teal-band: #8fd3cf;
    --salmon: #ef7b6e;
    --blush: #f3a19a;
    --lemon: #f7e81d;
    --lemon-band: #faf08a;
    --rose: #e8457c;
    --rose-band: #f19bb9;
    --charcoal: #141a1a;
    --charcoal-band: #8a8d8d;
    --chai-red: #c1272d;
    --white: #ffffff;
  }
  * { box-sizing: border-box; margin: 0; padding: 0; }
  html, body {
    width: 1200px; height: 1000px; overflow: hidden;
    background: var(--page);
    font-family: "Noto Serif", Georgia, serif;
  }
  .sheet { position: relative; width: 1200px; height: 1000px; }

  /* Round brand label */
  .round-label {
    position: absolute; left: 253px; top: 80px;
    width: 250px; height: 250px; border-radius: 50%;
    background: var(--teal-soft);
    border: 8px solid var(--teal);
    box-shadow: 6px 6px 6px var(--shadow);
    display: flex; align-items: center; justify-content: center;
  }
  .brand-name {
    color: var(--white); font-weight: 700; text-align: center;
    line-height: 1.25; letter-spacing: 0.5px;
  }
  .round-label .brand-name { font-size: 24px; }

  /* Rectangular ingredient label */
  .ingredient-label {
    position: absolute; left: 628px; top: 103px;
    width: 442px; height: 219px;
    background: var(--teal); color: var(--white);
    box-shadow: 7px 7px 6px var(--shadow);
  }
  .ingredient-label .tea-name {
    position: absolute; top: 10px; left: 0; width: 100%;
    text-align: center; font-size: 23px; font-weight: 700; letter-spacing: 2px;
  }
  .ingredient-label .rule {
    position: absolute; left: 27px; top: 52px; width: 392px; height: 4px;
    background: var(--white);
  }
  .ingredient-label .ingredients {
    position: absolute; left: 48px; top: 68px; width: 350px;
    font-size: 20px; line-height: 25.5px;
  }
  .ingredient-label .ingredients h3 { font-size: 20px; font-weight: 700; }
  .ingredient-label .ingredients p { font-weight: 400; }
  .ingredient-label .web {
    position: absolute; top: 180px; left: 0; width: 100%;
    text-align: center; font-size: 20px; letter-spacing: 0.5px;
  }

  /* Pack cards */
  .pack-card {
    position: absolute; width: 498px; height: 262px;
    background: var(--white); border: 1px solid var(--ink);
    box-shadow: 7px 7px 6px var(--shadow);
    overflow: hidden;
  }
  .pack-card .tea-name {
    position: absolute; top: 25px; left: 0; width: 100%;
    text-align: center; font-size: 22px; font-weight: 400; letter-spacing: 0.8px;
  }
  .pack-card .band {
    position: absolute; left: 0; right: 0; top: 138px; bottom: 0;
    border-top: 3px solid var(--tone);
    background: var(--band);
  }
  .pack-card .badge {
    position: absolute; left: 156px; top: 76px;
    width: 186px; height: 186px; border-radius: 50%;
    background: var(--tone);
    border: 6px solid var(--white);
    box-shadow: 0 0 0 4px var(--tone);
    display: flex; align-items: center; justify-content: center;
  }
  .pack-card .brand-name { font-size: 18px; color: var(--mark-text, var(--white)); }

  .card-chamomile { left: 88px;  top: 375px; --tone: var(--teal); --band: var(--teal-band); }
  .card-chamomile .badge { background: var(--teal-soft); }
  .card-lemongrass { left: 616px; top: 375px; --tone: var(--lemon); --band: var(--lemon-band); --mark-text: #6f6300; }
  .card-breakfast { left: 88px;  top: 668px; --tone: var(--rose); --band: var(--rose-band); }
  .card-chai { left: 616px; top: 668px; --tone: var(--charcoal); --band: var(--charcoal-band); }

  .card-chamomile .tea-name { color: var(--salmon); }
  .card-lemongrass .tea-name { color: var(--blush); }
  .card-breakfast .tea-name { color: var(--teal); }
  .card-chai .tea-name { color: var(--chai-red); }
</style>
</head>
<body>
<main class="sheet">

  <div class="round-label">
    <span class="brand-name">Tarrowby<br>Tea Company</span>
  </div>

  <section class="ingredient-label">
    <h2 class="tea-name">Chamomile Silver Tide</h2>
    <div class="rule"></div>
    <div class="ingredients">
      <h3>Ingredients</h3>
      <p>Chamomile flowers, spearmint leaf, calendula petals and rosehip shells</p>
    </div>
    <p class="web">www.corvalbrewhouse.com.au</p>
  </section>

  <section class="pack-card card-chamomile">
    <h2 class="tea-name">Chamomile Silver Tide</h2>
    <div class="band" role="img" aria-label="Fine vertical pinstripe band in teal"></div>
    <div class="badge"><span class="brand-name">Tarrowby<br>Tea Company</span></div>
  </section>

  <section class="pack-card card-lemongrass">
    <h2 class="tea-name">Lemongrass &amp; Ginger</h2>
    <div class="band" role="img" aria-label="Fine vertical pinstripe band in yellow"></div>
    <div class="badge"><span class="brand-name">Tarrowby<br>Tea Company</span></div>
  </section>

  <section class="pack-card card-breakfast">
    <h2 class="tea-name">English Breakfast</h2>
    <div class="band" role="img" aria-label="Fine vertical pinstripe band in pink"></div>
    <div class="badge"><span class="brand-name">Tarrowby<br>Tea Company</span></div>
  </section>

  <section class="pack-card card-chai">
    <h2 class="tea-name">Black Chai</h2>
    <div class="band" role="img" aria-label="Fine vertical pinstripe band in black"></div>
    <div class="badge"><span class="brand-name">Tarrowby<br>Tea Company</span></div>
  </section>

</main>
</body>
</html>
```